Zine template for Velvet Orchard Zine

I wanted to create a zine template in inDesign or but could use some design expertise.  I have attached my draft doc.  the zine will sometimes be 32 pages, or 40 pages (8.5inches x 11, folded in 1/2). the publicaton is photocopied so placing pages in right order is important for easier assembly. I can attach sample.
I am open to masthead improvement (velvet orchard...stories you can touch).  But needs to look more like "hand made" -not too slick.  I am open to changing icon (pen dipping in water making waves...) to something that suggests a tactile, sensory impact.
I will fill in content myself for each edition.  But need page set ups that is column grid based.  So I can play with layout.  But wanted  a core based design that can make sure each edition is coherent.
Title page-same format but of course different theme, main pic, and contents
Letter from Editor/Table of Contents-again, format same, but content will change
Need 1 double page layout with double column layout option
1 double page layout with single column layout option
Maybe one with triple column layout option.
Common page number format-using shoe icon
I like idea of common theme based header or footer on each page
Add bus card info under Brindlewick press
Needs to have at least 1/2 inch margin around edges as it is copied and don't want content to bleed off page.
REmember pages stapled so need enough space between columns in middle to allow for staple and still read content
DOes this make sense?  Essentially looking for a mag layout for zine (which is just using std letter size paper, folder, and stapled to make a zine (like a pamphlet).  I uploaded a few samples of layouts and how the pages work.
Let me know if you have questions!

```html
<!DOCTYPE html>
<html lang="la">
<head>
<meta charset="utf-8">
<title>Velvet Orchard Zine – Spread 2–3</title>
<link rel="stylesheet" href="https://fonts.googleapis.com/css2?family=Crimson+Text:wght@400&family=Bodoni+Moda:wght@400&display=swap">
<style>
  :root {
    --paper: #ffffff;
    --ink: #1d1d1d;
    --rule: #111111;
    --icon-tone: #2a2a2a;
  }
  html, body {
    margin: 0;
    padding: 0;
    overflow: hidden;
    background: var(--paper);
  }
  .spread {
    position: relative;
    width: 1200px;
    height: 779px;
    box-sizing: border-box;
    border: 4px solid var(--rule);
    background: var(--paper);
    color: var(--ink);
    font-family: "Crimson Text", Georgia, serif;
    overflow: hidden;
  }
  .masthead-name {
    position: absolute;
    left: 58px;
    top: 36px;
    margin: 0;
    font-family: "Crimson Text", Georgia, serif;
    font-weight: 400;
    font-size: 20px;
    line-height: 19px;
    letter-spacing: 0.3px;
    text-transform: uppercase;
    color: var(--ink);
  }
  .issue-label {
    position: absolute;
    left: 1004px;
    top: 38px;
    margin: 0;
    font-family: "Bodoni Moda", "Times New Roman", serif;
    text-transform: uppercase;
    color: var(--ink);
  }
  .issue-label .volume {
    display: block;
    font-size: 23px;
    line-height: 24px;
  }
  .issue-label .tagline {
    display: block;
    font-size: 11.5px;
    line-height: 13px;
  }
  .column {
    position: absolute;
    width: 240px;
    margin: 0;
    font-size: 16.2px;
    line-height: 23.3px;
    white-space: nowrap;
  }
  .column p { margin: 0; }
  .column p + p { margin-top: 23.3px; }
  .col-1 { left: 62px; top: 160px; }
  .col-2 { left: 311px; top: 160px; }
  .col-3 { left: 666px; top: 160px; }
  .col-4 { left: 918px; top: 346px; }
  .drop-cap {
    float: left;
    font-size: 78px;
    line-height: 62px;
    margin: 4px 6px 0 -2px;
  }
  .image-frame {
    position: absolute;
    margin: 0;
    box-sizing: border-box;
    border: 1.5px solid var(--rule);
    display: flex;
    align-items: center;
    justify-content: center;
    font-family: "Bodoni Moda", "Times New Roman", serif;
    font-size: 17px;
    letter-spacing: 0.5px;
  }
  .frame-left { left: 311px; top: 481px; width: 224px; height: 163px; }
  .frame-right { left: 918px; top: 166px; width: 224px; height: 163px; }
  .footer-wave {
    position: absolute;
    left: 0;
    top: 670px;
    width: 1192px;
    height: 80px;
  }
  .shoe-icon {
    position: absolute;
    height: 30px;
    background: linear-gradient(160deg, var(--icon-tone), #555555);
    border-radius: 14px 5px 8px 8px;
  }
  .shoe-left { left: 44px; top: 690px; width: 56px; }
  .shoe-right { left: 1094px; top: 688px; width: 66px; }
  .folio {
    position: absolute;
    top: 724px;
    font-family: "Crimson Text", Georgia, serif;
    font-size: 17px;
    line-height: 17px;
  }
  .folio-left { left: 106px; }
  .folio-right { left: 1083px; }
</style>
</head>
<body>
<main class="spread">
  <header>
    <p class="masthead-name">Velvet<br>Orchard</p>
    <p class="issue-label">
      <span class="volume">Volume I</span>
      <span class="tagline">…content that<br>makes waves</span>
    </p>
  </header>

  <article class="column col-1">
    <p><span class="drop-cap">S</span>undem incim ium quam<br>receped maximi, nimaio<br>molut abo. Nam, sequos<br>rehendus aliquat emporpor<br>sim vendae voluptatus re mos<br>seceatempos sent que et quate<br>et vitate nos porporpos non<br>con reptatem sedi res serci<br>volumquae con cones eum<br>re ellorerae renihilibus, vent<br>untiorectur? Qui ut aut pe debis<br>am volendit esequod ut debit<br>eicipit dolutem ollenti verum<br>faccum quibus nullendi te mi,<br>venda alitatur re, optatur?</p>
    <p>Ihicilit, totati dis a solorpo<br>reperit voluptatur? Elitat quodis<br>et perion et repro qundi<br>dolorerione venditi orporest<br>qui officiunt et liquam in nieni</p>
  </article>

  <section class="column col-2">
    <p>untia quunt quas quation et a<br>venim quiandelSed que sunt<br>quis duciis abore disit quam<br>aut.Nonet fugia sitatem fugiam.<br>Apisimai onsequa ssento<br>molessit aut veritas pissitatum<br>faceriae similiq uatqui bernate<br>pe sed quae dit explis que<br>num, seditat asperum ad<br>mi, ut pra doluptu riorpos<br>maximillesti cupta autati tem<br>doluptatisXerum sanihit od<br>quis represt ianihil.</p>
  </section>

  <figure class="image-frame frame-left">IMAGE</figure>

  <section class="column col-3">
    <p>Fuga. Nam as vendus enisque<br>volupta speditibus, cum nus<br>a velictur? Quist fugitate plab<br>inctur rem dolorum eossecea<br>eum apicae cor sequunde<br>paria voloressi dolupta tiust,<br>volupta temquidi ad qui blabo.<br>As nemporum volupta ne<br>volores atiaspelites audiandis<br>sae dolupta temque nobis am<br>quissime site cum nimperis<br>aut officabore, ex et, sim et<br>fugitium volorio rehendes<br>quidebis ex ent re nam site<br>nem que officiusti od quas nis<br>quis sinimuscid maximolorro<br>berspediam fugita nectur<br>sequist eniat parum, acest fugia<br>quiasitatum aut as quosam<br>nempos maiorehenem sequiat<br>quia preicium eumque iuntet</p>
  </section>

  <figure class="image-frame frame-right">IMAGE</figure>

  <section class="column col-4">
    <p>dolorepti as aperionsed quo<br>maximus et magnat. Agnient.<br>Cum apiet as eum.Cus, tem<br>hilliatia consequ iaecta nonse<br>peruntio. Agnimin ullibus.<br>Sed ulparum et ma nimpor<br>am untia cum lat. Ullacius.<br>Giandic tasimo bere.Um fuga.<br>Alia solupta tissequo volupti<br>nusandis num volupisOluptatas<br>ad ute quia sunt. Imossitiur?<br>MinciusanitNum sam rerferia.</p>
  </section>

  <footer>
    <svg class="footer-wave" viewBox="0 0 1192 80" aria-hidden="true">
      <path d="M0 42 C 20 45, 38 48, 52 50" fill="none" stroke="var(--rule)" stroke-width="1.6"/>
      <path d="M122 32 C 300 20, 480 46, 640 50 C 800 54, 960 44, 1080 40" fill="none" stroke="var(--rule)" stroke-width="1.8"/>
      <path d="M1150 26 C 1168 20, 1180 14, 1192 10" fill="none" stroke="var(--rule)" stroke-width="1.6"/>
    </svg>
    <div class="shoe-icon shoe-left" role="img" aria-label="Small black high-heel shoe icon marking the page number"></div>
    <span class="folio folio-left">2</span>
    <div class="shoe-icon shoe-right" role="img" aria-label="Small black high-heel shoe icon marking the page number"></div>
    <span class="folio folio-right">3</span>
  </footer>
</main>
</body>
</html>
```